Copperleaf Keystone Method

We are a wealth advisory firm. We need a design that shows our business is built on seven pillars. These seven pillars support all 85 things. These seven pillars form the foundation of our process. As their lives unfold and their needs evolve, they can’t outgrow our process; they’ll grow into it as critical life events occur and their lives progress.

We have an example of pillars, a figure of 8, and trees—we would like it to be modern, clean, and nature-inspired. If you use pillars, they cannot look 80s or like a law office. I am also attaching a picture of our logo and the landing page of our website for reference to our feel and style.
We want to use the language on the sheet with figure 8 in the final design.

Target Market(s)

families and small business owners with 1 million + of investable assets

Industry/Entity Type

Finance

Font styles to use
Sans Serif

Colors
0054AA
0677BA
7BADD7
CADEEF
E8F1F8
FFC000
F8CF3A
FAE287
FDF2CF
FEFAEE
EE7325
F08F49
F5BC92
FAE3D3
FDF4ED

```html
<!DOCTYPE html>
<html lang="en">
<head>
<meta charset="utf-8">
<title>Copperleaf Keystone Method</title>
<link href="https://fonts.googleapis.com/css2?family=Montserrat:wght@500;600;800;900&family=Oswald:wght@500&display=swap" rel="stylesheet">
<style>
  :root {
    --canvas: #e8f1f8;
    --deep-blue: #0054aa;
    --mid-blue: #0677ba;
    --soft-blue: #7badd7;
    --pale-blue: #cadeef;
    --gold: #ffc000;
    --orange: #ee7325;
    --orange-glow: rgba(240, 143, 73, 0.65);
    --cream: #fefaee;
    --white: #ffffff;
  }
  * { margin: 0; padding: 0; box-sizing: border-box; }
  html, body { width: 812px; height: 1200px; overflow: hidden; }
  body { background: var(--canvas); position: relative; font-family: "Montserrat", sans-serif; }

  .poster {
    position: absolute; left: 0; top: 287px;
    width: 812px; height: 625px;
    background: var(--deep-blue);
  }
  .connectors { position: absolute; inset: 0; width: 812px; height: 625px; }

  .brand {
    position: absolute; top: 44px; left: 0; width: 100%;
    display: flex; justify-content: center; align-items: center; gap: 12px;
  }
  .brand-mark { width: 40px; height: 40px; border-radius: 50%; background: var(--white); }
  .brand-name {
    color: var(--white); font-weight: 500;
    font-size: 22px; letter-spacing: 3px; line-height: 1.05;
  }

  .headline {
    position: absolute; top: 130px; left: 0; width: 100%; text-align: center;
    font-weight: 800; font-size: 36px; line-height: 44px; color: var(--white);
    letter-spacing: 0.5px; white-space: nowrap;
  }
  .headline .accent { color: var(--gold); }

  .tagline {
    position: absolute; top: 191px; left: 153px; width: 506px; height: 32px;
    border-radius: 16px; background: var(--mid-blue); color: var(--white);
    font-weight: 800; font-size: 16.5px; display: flex; align-items: center; justify-content: center;
    white-space: nowrap;
  }

  .hub {
    position: absolute; left: 380px; top: 238px; width: 52px; height: 52px; border-radius: 50%;
    background: var(--orange); border: 2px solid var(--deep-blue); box-shadow: 0 0 0 2px var(--orange);
  }

  .pillars {
    position: absolute; top: 304px; left: 42px; display: flex; gap: 14px;
  }
  .pillar {
    position: relative; width: 92px; height: 155px; background: var(--cream); border-radius: 8px;
    box-shadow: 0 0 7px 1px var(--orange-glow);
    display: flex; flex-direction: column; align-items: center; padding-top: 10px;
  }
  .pillar-number {
    font-family: "Oswald", sans-serif; font-weight: 500; font-size: 31px; line-height: 1;
    color: var(--deep-blue);
  }
  .pillar-rule { width: 18px; height: 2px; background: var(--orange); margin: 10px 0 7px; }
  .pillar-label {
    font-weight: 600; font-size: 10px; line-height: 1.3; color: var(--deep-blue); text-align: center;
  }
  .pillar-icon { position: absolute; top: 110px; left: 30px; width: 32px; height: 32px; fill: var(--soft-blue); }
  .pillar-dot {
    position: absolute; bottom: -6px; left: 40px; width: 12px; height: 12px; border-radius: 50%;
    background: var(--orange); border: 2px solid var(--white);
  }

  .total {
    position: absolute; left: 323px; top: 532px; width: 166px; height: 33px; border-radius: 17px;
    background: var(--orange); color: var(--white); font-weight: 900; font-size: 22px;
    display: flex; align-items: center; justify-content: center; letter-spacing: 0.3px;
  }
</style>
</head>
<body>
<main class="poster">
  <svg class="connectors" viewBox="0 0 812 625" aria-hidden="true">
    <g fill="none" stroke="#f5bc92" stroke-width="1.4" stroke-dasharray="2 2.5">
      <path d="M88 465 V575 q0 10 10 10 H330 q10 0 10 -10 V565"/>
      <path d="M194 465 V538 q0 10 10 10 H323"/>
      <path d="M300 465 V500 q0 10 10 10 H345 q10 0 10 10 V532"/>
      <path d="M406 465 V532"/>
      <path d="M512 465 V500 q0 10 -10 10 H467 q-10 0 -10 10 V532"/>
      <path d="M618 465 V538 q0 10 -10 10 H489"/>
      <path d="M724 465 V575 q0 10 -10 10 H482 q-10 0 -10 -10 V565"/>
    </g>
  </svg>

  <header class="brand">
    <span class="brand-mark"></span>
    <span class="brand-name">NORTHVALE<br>CAPITAL</span>
  </header>

  <h1 class="headline">COPPERLEAF KEYSTONE <span class="accent">METHOD</span></h1>
  <p class="tagline">OUR PROCESS EVOLVES AS YOUR LIFE UNFOLDS</p>
  <div class="hub"></div>

  <section class="pillars">
    <article class="pillar">
      <span class="pillar-number">01</span><span class="pillar-rule"></span>
      <span class="pillar-label">Wealth<br>Management</span>
      <svg class="pillar-icon" viewBox="0 0 30 30"><path d="M15 2 L28 9 H2 Z"/><rect x="3" y="10" width="24" height="2"/><rect x="5" y="13" width="3" height="11"/><rect x="10" y="13" width="3" height="11"/><rect x="17" y="13" width="3" height="11"/><rect x="22" y="13" width="3" height="11"/><rect x="2" y="25" width="26" height="3"/></svg>
      <span class="pillar-dot"></span>
    </article>
    <article class="pillar">
      <span class="pillar-number">02</span><span class="pillar-rule"></span>
      <span class="pillar-label">Risk<br>Management</span>
      <svg class="pillar-icon" viewBox="0 0 30 30"><path d="M15 2 L29 28 H1 Z"/><rect x="13.5" y="10" width="3" height="10" fill="#fefaee"/><circle cx="15" cy="23.5" r="1.7" fill="#fefaee"/></svg>
      <span class="pillar-dot"></span>
    </article>
    <article class="pillar">
      <span class="pillar-number">03</span><span class="pillar-rule"></span>
      <span class="pillar-label">Tax<br>Planning</span>
      <svg class="pillar-icon" viewBox="0 0 30 30"><ellipse cx="14" cy="16" rx="11" ry="8"/><rect x="7" y="21" width="4" height="6"/><rect x="16" y="21" width="4" height="6"/><path d="M24 14 L29 12 V19 L24 18 Z"/><circle cx="20" cy="13" r="1.2" fill="#fefaee"/></svg>
      <span class="pillar-dot"></span>
    </article>
    <article class="pillar">
      <span class="pillar-number">04</span><span class="pillar-rule"></span>
      <span class="pillar-label">Estate<br>Planning</span>
      <svg class="pillar-icon" viewBox="0 0 30 30"><rect x="2" y="14" width="8" height="14"/><rect x="11" y="4" width="8" height="24"/><rect x="20" y="10" width="8" height="18"/><g fill="#fefaee"><rect x="4" y="17" width="2" height="2"/><rect x="4" y="22" width="2" height="2"/><rect x="13" y="8" width="2" height="2"/><rect x="13" y="13" width="2" height="2"/><rect x="13" y="18" width="2" height="2"/><rect x="22" y="14" width="2" height="2"/><rect x="22" y="19" width="2" height="2"/></g></svg>
      <span class="pillar-dot"></span>
    </article>
    <article class="pillar">
      <span class="pillar-number">05</span><span class="pillar-rule"></span>
      <span class="pillar-label">Cash<br>Management</span>
      <svg class="pillar-icon" viewBox="0 0 30 30"><path d="M3 11 L24 5 L26 10 Z"/><path d="M2 12 H28 V26 H2 Z M4.5 14.5 V23.5 H25.5 V14.5 Z"/><circle cx="15" cy="19" r="3"/><circle cx="8" cy="19" r="1"/><circle cx="22" cy="19" r="1"/></svg>
      <span class="pillar-dot"></span>
    </article>
    <article class="pillar">
      <span class="pillar-number">06</span><span class="pillar-rule"></span>
      <span class="pillar-label">Philanthropy</span>
      <svg class="pillar-icon" viewBox="0 0 30 30"><path d="M15 28 L3.5 15.5 C-1 10 3 3 8.5 3.5 C11.5 3.8 13.5 6 15 8 C16.5 6 18.5 3.8 21.5 3.5 C27 3 31 10 26.5 15.5 Z"/></svg>
      <span class="pillar-dot"></span>
    </article>
    <article class="pillar">
      <span class="pillar-number">07</span><span class="pillar-rule"></span>
      <span class="pillar-label">Value Added<br>Services</span>
      <svg class="pillar-icon" viewBox="0 0 30 30"><path d="M11 5 H19 V9 H17 V7 H13 V9 H11 Z"/><rect x="2" y="9" width="26" height="8" rx="1.5"/><rect x="2" y="18.5" width="26" height="9" rx="1.5"/><rect x="13" y="15" width="4" height="5"/></svg>
      <span class="pillar-dot"></span>
    </article>
  </section>

  <p class="total">85 THINGS</p>
</main>
</body>
</html>
```